Investment company needing business card

We are wanting a business card which looks sharp and easy on the eye. We are thinking of having a business card with the logo embossed on it, to really make it stand out. We will only have a small amount of information of the business card, person's name, position, email address and phone number

Danielle Hartig
Executive Assistant
+64 21 574 3162
danielleh@quarvendale.co.nz

Requirements
Must have
• Embossed logo
Should not have
• Not to be busy

```html
<!DOCTYPE html>
<html lang="en">
<head>
<meta charset="utf-8">
<title>Quarvendale – Business Card</title>
<link href="https://fonts.googleapis.com/css2?family=Catamaran:wght@300;400;600;700&display=swap" rel="stylesheet">
<style>
  :root {
    --bg: #1c1c1c;
    --card-light: #f1f1f1;
    --card-dark: #232323;
    --green: #1fb56b;
    --grey: #6b6b6b;
    --text: #555555;
    --rule: #707070;
  }
  * { margin: 0; padding: 0; box-sizing: border-box; }
  html, body { width: 1200px; height: 896px; overflow: hidden; }
  body {
    background: var(--bg);
    font-family: "Catamaran", sans-serif;
    position: relative;
  }
  .card {
    position: absolute;
    left: 351px;
    width: 490px;
    height: 278px;
    overflow: hidden;
  }
  .card-front { top: 160px; background: var(--card-light); }
  .card-back { top: 470px; background: var(--card-dark); }

  .brand {
    position: absolute;
    display: flex;
    align-items: center;
    gap: 8px;
  }
  .brand-mark {
    width: 16px;
    height: 16px;
    background: var(--green);
  }
  .brand-name {
    font-weight: 700;
    font-size: 25px;
    letter-spacing: 0.5px;
    color: var(--green);
    line-height: 1;
  }
  .card-front .brand { left: 28px; top: 126px; }
  .card-back .brand { left: 50%; top: 127px; transform: translateX(-50%); }

  .divider {
    position: absolute;
    left: 274px;
    top: 73px;
    width: 1px;
    height: 132px;
    background: var(--rule);
  }
  .contact {
    position: absolute;
    left: 295px;
    top: 72px;
    color: var(--text);
    font-weight: 300;
    font-size: 11px;
    line-height: 1.2;
  }
  .person-name {
    font-weight: 600;
    font-size: 18px;
    color: var(--green);
    line-height: 1.1;
  }
  .person-role { margin-top: 4px; }
  .address { margin-top: 8px; line-height: 17px; }
  .contact-list { list-style: none; margin-top: 6px; }
  .contact-list li {
    display: flex;
    align-items: center;
    gap: 6px;
    height: 17.5px;
  }
  .contact-list svg { width: 9px; height: 9px; flex: none; }

  .footer-band {
    position: absolute;
    left: 0;
    bottom: 0;
    width: 490px;
    height: 6px;
  }
</style>
</head>
<body>
  <section class="card card-front">
    <div class="brand">
      <span class="brand-mark"></span>
      <span class="brand-name">QUARVENDALE</span>
    </div>
    <div class="divider"></div>
    <div class="contact">
      <p class="person-name">Danielle Hartig</p>
      <p class="person-role">Executive Assistant</p>
      <p class="address">1845 Marlowe Street San<br>Diego, CA 92116</p>
      <ul class="contact-list">
        <li>
          <svg viewBox="0 0 10 10" aria-hidden="true"><path fill="#1fb56b" d="M2 0.5 L3.6 0.5 L4.3 2.8 L3.2 3.8 Q4.3 6 6.3 6.9 L7.2 5.8 L9.5 6.5 L9.5 8.2 Q9.3 9.6 7.8 9.5 Q1 8.6 0.5 2 Q0.5 0.6 2 0.5Z"/></svg>
          +64 21 574 3162
        </li>
        <li>
          <svg viewBox="0 0 10 10" aria-hidden="true"><rect x="0.6" y="1.8" width="8.8" height="6.4" fill="none" stroke="#1fb56b" stroke-width="1"/><path d="M0.6 1.8 L5 5.6 L9.4 1.8" fill="none" stroke="#1fb56b" stroke-width="1"/></svg>
          danielleh@quarvendale.co.nz
        </li>
        <li>
          <svg viewBox="0 0 10 10" aria-hidden="true"><g fill="none" stroke="#1fb56b" stroke-width="0.9"><circle cx="5" cy="5" r="4.3"/><ellipse cx="5" cy="5" rx="1.9" ry="4.3"/><path d="M0.7 5 H9.3 M1.4 2.8 H8.6 M1.4 7.2 H8.6"/></g></svg>
          www.quarvendale.co.nz
        </li>
      </ul>
    </div>
    <svg class="footer-band" viewBox="0 0 490 6" preserveAspectRatio="none" aria-hidden="true">
      <polygon points="0,0 276,0 270,6 0,6" fill="var(--green)"/>
      <polygon points="280,0 490,0 490,6 274,6" fill="var(--grey)"/>
    </svg>
  </section>

  <section class="card card-back">
    <div class="brand">
      <span class="brand-mark"></span>
      <span class="brand-name">QUARVENDALE</span>
    </div>
  </section>
</body>
</html>
```